Bref créative
Stationary, Envelope, and Business Card Designs for an Accounting/Bookkeeping company
R&K Ledger and Audit Partners, LLC
Professional
Doug M. Prentt
Partner, Chief Financial Officer
41207 Route 53
Brookvale, FL 00000
dprentt@rkbooksco.com
www.rkbooksco.com
R&K Ledger and Audit Partners, LLC Logo in AI format - full color.
Logo color specifics.

```html
<!DOCTYPE html>
<html lang="en">
<head>
<meta charset="utf-8">
<title>Ledger and Audit Partners – Stationery Set</title>
<link href="https://fonts.googleapis.com/css2?family=Open+Sans:wght@400;600;700&display=swap" rel="stylesheet">
<style>
:root{
  --bg-dark:#3a3b3d;
  --bg-light:#6b6c6f;
  --brand-blue:#1565b8;
  --brand-navy:#0b3f82;
  --brand-green:#4aa83a;
  --brand-lime:#8cc63f;
  --paper:#ffffff;
  --ink:#4a4f57;
  --muted:#9aa2ac;
}
*{margin:0;padding:0;box-sizing:border-box}
html,body{width:1200px;height:240px;overflow:hidden}
body{
  font-family:"Open Sans",Arial,sans-serif;
  background:radial-gradient(ellipse at 50% 40%,var(--bg-light),var(--bg-dark) 80%);
  position:relative;color:var(--ink);
}
.item{position:absolute;background:var(--paper);overflow:hidden;box-shadow:0 1px 3px rgba(0,0,0,.45)}
.wave{position:absolute;left:0;bottom:0;width:100%;display:block}
.brand-name{position:absolute;font-weight:700;line-height:1.15;color:var(--brand-blue)}
.brand-lockup{left:22px;top:32px;width:120px;font-size:12px;color:#fff}
.tiny{font-size:3px;line-height:1.45;color:var(--ink)}
.card-front{left:12px;top:108px;width:132px;height:50px}
.card-front .brand-name{left:6px;top:7px;width:58px;font-size:5px}
.card-front .contact{position:absolute;right:6px;top:7px;text-align:right}
.card-back{left:12px;top:166px;width:132px;height:50px;background:linear-gradient(120deg,var(--brand-lime),var(--brand-green) 60%,#2f8a2d)}
.card-back .brand-name{left:8px;top:12px;width:90px;font-size:7px;color:#fff}
.letterhead{top:12px;width:137px;height:198px}
.letterhead.one{left:156px}.letterhead.two{left:307px}
.letterhead .brand-name{left:10px;top:10px;width:70px;font-size:5px}
.letterhead .body{position:absolute;left:12px;right:14px;top:46px}
.letterhead .body p{margin-bottom:2px}
.letterhead .sign{position:absolute;left:12px;top:138px;width:30px;height:1px;background:var(--muted)}
.letterhead .footer{position:absolute;left:0;right:0;bottom:3px;text-align:center;color:#fff;z-index:2}
.slip{left:456px;width:108px;height:36px}
.slip.a{top:96px}.slip.b{top:151px;height:46px}
.slip .brand-name{left:6px;top:5px;width:60px;font-size:4px}
.envelope{left:576px;width:144px}
.envelope.green{top:96px;height:48px;background:linear-gradient(180deg,#fff,#f1f5f2)}
.envelope.plain{top:153px;height:52px}
.envelope .brand-name{left:6px;top:4px;width:60px;font-size:4px;z-index:2}
.envelope.green .brand-name{color:#fff}
.folder-back{left:739px;top:12px;width:162px;height:216px;background:radial-gradient(circle at 55% 45%,#2f8fe0,var(--brand-navy) 75%)}
.folder-front{left:907px;top:12px;width:168px;height:216px;background:radial-gradient(circle at 50% 35%,#3a9be6,var(--brand-blue) 45%,var(--brand-navy) 90%)}
.folder-front .brand-name{right:12px;top:142px;width:80px;text-align:right;font-size:6px;color:#fff}
.pocket{position:absolute;left:0;bottom:0;width:100%;height:70px}
</style>
</head>
<body>

<div class="brand-name brand-lockup">R&amp;K Ledger and Audit Partners, LLC</div>

<div class="item card-front">
  <div class="brand-name">R&amp;K Ledger and Audit Partners, LLC</div>
  <div class="contact tiny">
    <strong>Account Partner</strong><br>Finance and Tax Lead<br>Main Office, Suite 4<br>Brookvale, FL 00000<br>office@ledgeraudit.test<br>www.ledgeraudit.test
  </div>
  <svg class="wave" viewBox="0 0 132 16" height="16" preserveAspectRatio="none">
    <path d="M0 10 Q50 0 132 8 L132 16 L0 16Z" fill="var(--brand-blue)"/>
    <path d="M0 8 Q55 -2 132 5 L132 7 Q55 1 0 11Z" fill="var(--brand-green)"/>
  </svg>
</div>

<div class="item card-back">
  <div class="brand-name">R&amp;K Ledger and Audit Partners, LLC</div>
  <svg class="wave" viewBox="0 0 132 14" height="14" preserveAspectRatio="none">
    <path d="M0 9 Q60 0 132 7 L132 14 L0 14Z" fill="var(--brand-blue)"/>
  </svg>
</div>

<div class="item letterhead one">
  <div class="brand-name">R&amp;K Ledger and Audit Partners, LLC</div>
  <div class="body tiny">
    <p>Dear Client,</p>
    <p>Thank you for trusting our team with your books and tax filings this year.</p>
    <p>Sincerely,</p>
  </div>
  <div class="sign"></div>
  <svg class="wave" viewBox="0 0 137 30" height="30" preserveAspectRatio="none">
    <path d="M0 16 Q60 2 137 14 L137 30 L0 30Z" fill="var(--brand-blue)"/>
    <path d="M0 13 Q60 -2 137 10 L137 13 Q60 2 0 16Z" fill="var(--brand-green)"/>
  </svg>
  <div class="footer tiny" style="color:#fff">Main Office, Suite 4 · Brookvale, FL 00000 · www.ledgeraudit.test</div>
</div>

<div class="item letterhead two">
  <div class="brand-name">R&amp;K Ledger and Audit Partners, LLC</div>
  <div class="body tiny">
    <p>Dear Client,</p>
    <p>Thank you for trusting our team with your books and tax filings this year.</p>
    <p>Sincerely,</p>
  </div>
  <div class="sign"></div>
  <svg class="wave" viewBox="0 0 137 30" height="30" preserveAspectRatio="none">
    <path d="M0 16 Q60 2 137 14 L137 30 L0 30Z" fill="var(--brand-blue)"/>
    <path d="M0 13 Q60 -2 137 10 L137 13 Q60 2 0 16Z" fill="var(--brand-green)"/>
  </svg>
  <div class="footer tiny" style="color:#fff">Main Office, Suite 4 · Brookvale, FL 00000 · www.ledgeraudit.test</div>
</div>

<div class="item slip a">
  <div class="brand-name">R&amp;K Ledger and Audit Partners, LLC</div>
  <svg class="wave" viewBox="0 0 108 14" height="14" preserveAspectRatio="none">
    <path d="M0 9 Q45 0 108 7 L108 14 L0 14Z" fill="var(--brand-blue)"/>
    <path d="M0 7 Q45 -2 108 5 L108 7 Q45 0 0 9Z" fill="var(--brand-green)"/>
  </svg>
</div>
<div class="item slip b">
  <div class="brand-name">R&amp;K Ledger and Audit Partners, LLC</div>
  <svg class="wave" viewBox="0 0 108 16" height="16" preserveAspectRatio="none">
    <path d="M0 10 Q45 0 108 8 L108 16 L0 16Z" fill="var(--brand-blue)"/>
    <path d="M0 8 Q45 -2 108 6 L108 8 Q45 0 0 10Z" fill="var(--brand-green)"/>
  </svg>
</div>

<div class="item envelope green">
  <svg class="wave" viewBox="0 0 144 48" height="48" preserveAspectRatio="none" style="top:0">
    <path d="M0 0 L144 0 L144 14 Q72 34 0 14Z" fill="var(--brand-green)"/>
    <path d="M0 14 Q72 34 144 14 L144 18 Q72 38 0 18Z" fill="var(--brand-blue)"/>
  </svg>
  <div class="brand-name">R&amp;K Ledger and Audit Partners, LLC</div>
</div>
<div class="item envelope plain">
  <div class="brand-name">R&amp;K Ledger and Audit Partners, LLC</div>
  <svg class="wave" viewBox="0 0 144 52" height="52" preserveAspectRatio="none">
    <path d="M0 0 L72 30 L144 0" fill="none" stroke="#d7dce2" stroke-width=".8"/>
    <path d="M0 44 Q70 34 144 42 L144 52 L0 52Z" fill="var(--brand-blue)"/>
  </svg>
</div>

<div class="item folder-back">
  <svg class="pocket" viewBox="0 0 162 70" preserveAspectRatio="none">
    <path d="M0 30 Q80 10 162 26 L162 70 L0 70Z" fill="#ffffff"/>
    <path d="M0 26 Q80 6 162 22 L162 26 Q80 10 0 30Z" fill="var(--brand-green)"/>
  </svg>
</div>
<div class="item folder-front">
  <div class="brand-name">R&amp;K Ledger and Audit Partners, LLC</div>
  <svg class="pocket" viewBox="0 0 168 70" preserveAspectRatio="none">
    <path d="M0 34 Q90 12 168 30 L168 70 L0 70Z" fill="#ffffff"/>
    <path d="M0 30 Q90 8 168 26 L168 30 Q90 12 0 34Z" fill="var(--brand-green)"/>
  </svg>
</div>

</body>
</html>
```